Black Friday Sale Social Media Graphics

Focusing on Black Friday Graphics for each of the pics attached.  So need the product pics turned into  social media graphics (square size). For the color scheme of the graphics, they should all be complementary to the product colors.
You can add any of the stock photography attached but none are required. I mainly need BOLD text that says:
Black Friday Sale
Up to $15 Off
If you wanted to add smaller text, these headlines can work:
1.	Burn Belly Fat Fast!
2.	Double Your Weight Loss With Our Supplements!
3.	Lose Weight Naturally: Ditch the Prescription Pills & Needles!
4.	Tired of Stubborn Belly Fat? Discover What Works!
5.	Melt Away Belly Fat Faster with Our Supplements!
6.	Struggling to Lose Weight? Discover the Ultimate Solution!
7.	Ready to Burn Fat Faster?

Target Market(s)
women trying to lose weight
Industry/Entity Type
health and wellness
Requirements
Must have
- the product pics attached

Nice to have
- Bold text that says: Black Friday Sale

```html
<!DOCTYPE html>
<html lang="en">
<head>
<meta charset="utf-8">
<title>Black Friday Sale Social Graphics</title>
<link rel="stylesheet" href="https://fonts.googleapis.com/css2?family=Montserrat:wght@700;800;900&family=Anton&family=Bangers&family=Dancing+Script:wght@700&family=Poppins:wght@500;700;800;900&display=swap">
<style>
:root{
  --board:#ececed;
  --white:#ffffff;
  --ink:#0b0b0b;
  --pink-hot:#e0409c;
  --pink-neon:#ff7fd0;
  --red:#c8161d;
  --green-deep:#0e3229;
  --green-dark:#071c17;
  --teal:#2e9e8a;
  --teal-band:#1f4a40;
  --purple-deep:#240824;
  --purple:#5a1048;
  --magenta:#d0469f;
  --smoke-red:#6b1010;
  --photo-light:#e8e5e6;
  --bottle:#f2f1f3;
}
*{margin:0;padding:0;box-sizing:border-box}
html,body{width:1200px;height:634px;overflow:hidden;background:var(--board)}
.board{position:relative;width:1200px;height:634px}
.tile{position:absolute;width:274px;height:274px;overflow:hidden;font-family:"Montserrat",sans-serif;color:var(--white)}
.abs{position:absolute;z-index:2}
.photo{position:absolute;z-index:1;background:linear-gradient(160deg,#d8b9a3,#a97f66)}
.products{position:absolute;z-index:1;border-radius:6px;background:linear-gradient(180deg,var(--bottle),#cfcdd3)}
.center{text-align:center;white-space:nowrap}

/* Tile 1 */
.t-pink{left:29px;top:32px;background:var(--pink-hot)}
.t-pink .black-tag{left:21px;top:29px;width:176px;height:51px;background:var(--ink);transform:rotate(-4deg);font:900 44px/51px "Montserrat",sans-serif;text-align:center}
.t-pink .friday-tag{left:48px;top:88px;width:150px;height:24px;background:var(--ink);font:800 19px/24px "Montserrat",sans-serif;transform:rotate(-3deg);text-align:center}
.t-pink .upto{left:34px;top:121px;font:800 9px "Montserrat",sans-serif}
.t-pink .price{left:68px;top:107px;font:900 29px "Montserrat",sans-serif;transform:rotate(-3deg)}
.t-pink .foot{left:0;top:244px;width:274px;height:30px;background:var(--ink);font:800 18px/30px "Montserrat",sans-serif}

/* Tile 2 */
.t-chalk{left:318px;top:33px;background:radial-gradient(circle at 50% 40%,#3a3a3a,#1c1c1c)}
.t-chalk .brush{font-family:"Bangers",sans-serif;transform:rotate(-6deg);text-shadow:3px 3px 0 var(--red)}
.t-chalk .l1{left:82px;top:8px;font-size:46px}
.t-chalk .l2{left:48px;top:45px;font-size:44px}
.t-chalk .streak{left:55px;top:95px;width:172px;height:45px;background:var(--red);transform:rotate(-7deg);border-radius:4px 18px 4px 18px}
.t-chalk .get{left:68px;top:112px;font:700 14px "Montserrat",sans-serif;transform:rotate(-7deg)}
.t-chalk .get-upto{left:70px;top:130px;font:700 9px "Montserrat",sans-serif;transform:rotate(-7deg)}
.t-chalk .off{left:104px;top:96px;font:900 28px "Montserrat",sans-serif;transform:rotate(-7deg)}
.t-chalk .foot{left:0;top:248px;width:274px;font:400 11px "Bangers",sans-serif;letter-spacing:.4px}

/* Tile 3 */
.t-green{left:608px;top:32px;background:radial-gradient(circle at 60% 30%,var(--green-deep),var(--green-dark))}
.t-green .plate{left:58px;top:27px;width:172px;height:58px;background:linear-gradient(90deg,#f4f4f4,#cfd6d4);transform:skewX(-14deg)}
.t-green .black{left:70px;top:19px;font:68px/1 "Anton",sans-serif;color:var(--teal);transform:skewX(-10deg)}
.t-green .friday{left:30px;top:82px;font:80px/1 "Anton",sans-serif;transform:skewX(-10deg);letter-spacing:-1px}
.t-green .sale{left:84px;top:166px;font:56px/1 "Anton",sans-serif;transform:skewX(-10deg)}
.t-green .sign{left:9px;top:196px;width:66px;height:26px;background:var(--white);border-radius:2px;color:var(--ink);text-align:center}
.t-green .sign b{display:block;font:800 5px/1 "Montserrat",sans-serif;padding-top:3px}
.t-green .sign span{font:900 13px/1 "Montserrat",sans-serif}
.t-green .band{left:0;top:234px;width:180px;height:25px;background:var(--teal-band);font:800 6.6px/1.6 "Montserrat",sans-serif;text-align:center;padding-top:3px;z-index:0}

/* Tile 4 */
.t-glow{left:898px;top:34px;background:radial-gradient(circle at 90% 70%,#6b1a5a,#0c0a0e 60%)}
.t-glow .black{left:0;top:18px;width:274px;font:900 50px/1 "Montserrat",sans-serif;text-shadow:0 0 8px var(--pink-neon),0 0 2px var(--pink-neon)}
.t-glow .friday{left:0;top:70px;width:274px;font:900 26px/1 "Montserrat",sans-serif;text-shadow:0 0 6px var(--pink-neon)}
.t-glow .sub{left:0;top:101px;width:274px;font:700 7.5px "Montserrat",sans-serif}
.t-glow .pill{left:100px;top:120px;width:146px;height:55px;border-radius:28px 10px 10px 28px;background:linear-gradient(90deg,#3a0f3d,var(--magenta))}
.t-glow .pill-upto{left:172px;top:121px;font:800 10px "Montserrat",sans-serif}
.t-glow .pill-price{left:134px;top:130px;font:900 42px/1 "Montserrat",sans-serif}
.t-glow .pill-off{left:218px;top:143px;font:900 13px "Montserrat",sans-serif;transform:rotate(-90deg)}

/* Tile 5 */
.t-retro{left:161px;top:324px;background:linear-gradient(180deg,var(--purple-deep) 0%,#1a0619 30%,var(--purple) 100%)}
.t-retro .q{left:0;top:28px;width:274px;font:800 9px "Montserrat",sans-serif}
.t-retro .black{left:0;top:46px;width:274px;font:900 44px/1 "Montserrat",sans-serif;color:var(--pink-neon);text-shadow:0 0 8px #ff4fb8}
.t-retro .friday{left:0;top:89px;width:274px;font:500 44px/1 "Poppins",sans-serif;color:transparent;-webkit-text-stroke:1.5px var(--white);letter-spacing:3px}
.t-retro .box{left:39px;top:132px;width:196px;height:25px;border:2px solid var(--magenta);font:800 13px/21px "Montserrat",sans-serif}
.t-retro .podium{left:32px;top:232px;width:203px;height:42px;z-index:0}

/* Tile 6 */
.t-collage{left:448px;top:326px;background:radial-gradient(circle at 40% 20%,#1c1f1e,#070707)}
.t-collage .band{left:25px;top:10px;width:218px;height:13px;background:#23352f;font:700 7px/13px "Poppins",sans-serif}
.t-collage .black{left:0;top:21px;width:274px;font:900 46px/1 "Poppins",sans-serif}
.t-collage .friday{left:0;top:62px;width:274px;font:800 43px/1 "Poppins",sans-serif;color:transparent;-webkit-text-stroke:1.3px var(--white);letter-spacing:2px}
.t-collage .script{left:166px;top:84px;font:700 36px/1 "Dancing Script",cursive;transform:rotate(-12deg)}
.t-collage .pill{left:57px;top:102px;width:96px;height:23px;border-radius:12px;background:linear-gradient(90deg,#0f3a33,var(--teal))}
.t-collage .pill-upto{left:64px;top:104px;font:800 7px/1.1 "Montserrat",sans-serif}
.t-collage .pill-price{left:79px;top:104px;font:800 17px/1 "Montserrat",sans-serif}
.t-collage .card{position:absolute;z-index:1;background:var(--white);padding:6px}
.t-collage .card .photo{position:static;width:100%;height:100%}

/* Tile 7 */
.t-ember{left:735px;top:326px;background:radial-gradient(circle at 20% 20%,var(--smoke-red),#120505 55%,#4a0c0c)}
.t-ember .q1{left:0;top:14px;width:274px;font:500 10px "Poppins",sans-serif}
.t-ember .q2{left:0;top:27px;width:274px;font:700 11px "Poppins",sans-serif}
.t-ember .ring{left:0;top:0;z-index:0}
.t-ember .word{font:900 37px/1 "Montserrat",sans-serif;text-shadow:2px 2px 0 var(--red)}
.t-ember .script{left:96px;top:178px;font:700 36px/1 "Dancing Script",cursive}
.t-ember .burst{left:173px;top:170px;width:80px;height:80px}
.t-ember .b-upto{left:173px;top:183px;width:80px;font:600 9px "Poppins",sans-serif;color:var(--ink)}
.t-ember .b-price{left:173px;top:193px;width:80px;font:800 28px/1 "Poppins",sans-serif;color:var(--ink)}
.t-ember .b-off{left:180px;top:223px;width:80px;font:600 9px "Poppins",sans-serif;color:var(--ink)}
</style>
</head>
<body>
<main class="board">

  <section class="tile t-pink">
    <div class="photo" style="left:150px;top:80px;width:124px;height:164px;background:linear-gradient(160deg,#c99a80,#8d6450)" role="img" aria-label="Smiling woman in sports top holding a bathroom scale"></div>
    <div class="products" style="left:48px;top:153px;width:56px;height:91px" role="img" aria-label="Liver Calm supplement bottle"></div>
    <div class="abs black-tag">BLACK</div>
    <div class="abs friday-tag">FRIDAY SALE</div>
    <div class="abs upto">UP TO</div>
    <div class="abs price">$15 OFF</div>
    <div class="abs foot center">BURN BELLY FAT FAST!</div>
  </section>

  <section class="tile t-chalk">
    <div class="abs brush l1">BLACK</div>
    <div class="abs brush l2">FRIDAY SALE</div>
    <div class="abs streak"></div>
    <div class="abs get">GET</div>
    <div class="abs get-upto">UP TO</div>
    <div class="abs off">$15 OFF</div>
    <div class="products" style="left:27px;top:148px;width:226px;height:88px" role="img" aria-label="Liver Calm, Tummy Calm, Hormone Calm and Sugar Calm supplement bottles"></div>
    <div class="abs foot center">DOUBLE YOUR WEIGHT LOSS WITH OUR SUPPLEMENTS !</div>
  </section>

  <section class="tile t-green">
    <div class="abs plate"></div>
    <div class="products" style="left:226px;top:113px;width:38px;height:161px" role="img" aria-label="LumaBalm cream tube by Vita Hearth"></div>
    <div class="products" style="left:178px;top:170px;width:52px;height:104px" role="img" aria-label="Hormone Calm supplement bottle"></div>
    <div class="abs black">BLACK</div>
    <div class="abs friday">FRIDAY</div>
    <div class="abs sale">SALE</div>
    <svg class="abs" style="left:0;top:0" width="274" height="274" aria-hidden="true">
      <path d="M42 159 L18 197 M42 159 L66 197" stroke="#ffffff" stroke-width="0.8" fill="none"/>
    </svg>
    <div class="abs sign"><b>UP TO</b><span>$15 OFF</span></div>
    <div class="abs band">LOSE WEIGHT NATURALLY<br>DITCH THE PRESCRIPTION PILLS &amp; NEEDLES!</div>
  </section>

  <section class="tile t-glow">
    <div class="abs black center">BLACK</div>
    <div class="abs friday center">FRIDAY SALE</div>
    <div class="abs sub center">Tired of Stubborn Belly Fat? Discover What Works!</div>
    <div class="photo" style="left:0;top:128px;width:100px;height:146px" role="img" aria-label="Smiling woman in lavender activewear pointing at the offer"></div>
    <div class="abs pill"></div>
    <div class="abs pill-upto">UP TO</div>
    <div class="abs pill-price">$15</div>
    <div class="abs pill-off">OFF</div>
    <div class="products" style="left:109px;top:204px;width:126px;height:70px" role="img" aria-label="Sugar Calm, Liver Calm and Tummy Calm supplement bottles"></div>
  </section>

  <section class="tile t-retro">
    <div class="abs q center">READY TO BURN FAT FASTER?</div>
    <div class="abs black center">BLACK</div>
    <div class="abs friday center">FRIDAY</div>
    <div class="abs box center">SALE UP TO $15 OFF</div>
    <svg class="abs podium" viewBox="0 0 203 42" aria-hidden="true">
      <rect x="0" y="10" width="203" height="32" fill="#f2b8cc"/>
      <ellipse cx="101.5" cy="10" rx="101.5" ry="10" fill="#fbd3e0"/>
    </svg>
    <div class="products" style="left:53px;top:174px;width:168px;height:70px" role="img" aria-label="Liver Calm, Tummy Calm, Hormone Calm and Sugar Calm bottles on a podium"></div>
  </section>

  <section class="tile t-collage">
    <div class="abs band center">Melt Away Belly Fat Faster with Our Supplements!</div>
    <div class="abs black center">BLACK</div>
    <div class="abs friday center">FRIDAY</div>
    <div class="abs script">Sale</div>
    <div class="abs pill"></div>
    <div class="abs pill-upto">UP<br>TO</div>
    <div class="abs pill-price">$15 OFF</div>
    <div class="card" style="left:4px;top:134px;width:90px;height:116px;transform:rotate(-9deg)"><div class="photo" style="background:var(--photo-light)" role="img" aria-label="Hormone Calm bottle and LumaBalm cream"></div></div>
    <div class="card" style="left:94px;top:132px;width:85px;height:100px"><div class="photo" style="background:linear-gradient(160deg,#7a5a47,#3b2a22)" role="img" aria-label="Woman in a kitchen presenting the supplement range"></div></div>
    <div class="card" style="left:183px;top:130px;width:86px;height:110px;transform:rotate(9deg)"><div class="photo" style="background:var(--photo-light)" role="img" aria-label="Sugar Calm, Liver Calm and Tummy Calm bottles"></div></div>
  </section>

  <section class="tile t-ember">
    <div class="abs q1 center">Struggling to Lose Weight?</div>
    <div class="abs q2 center">Discover the Ultimate Solution!</div>
    <svg class="abs ring" width="274" height="274" aria-hidden="true">
      <circle cx="137" cy="158" r="100" fill="none" stroke="#d11a1a" stroke-width="5"/>
    </svg>
    <div class="photo" style="left:0;top:142px;width:52px;height:132px" role="img" aria-label="Excited woman in grey activewear holding a bathroom scale"></div>
    <div class="abs word" style="left:62px;top:95px">BLACK</div>
    <div class="abs word" style="left:56px;top:134px">FRIDAY</div>
    <div class="abs script">Sale</div>
    <svg class="abs burst" viewBox="0 0 80 80" aria-hidden="true">
      <polygon fill="#ffffff" stroke="#d11a1a" stroke-width="2" points="40,2 47,12 59,7 61,20 74,21 70,33 80,40 70,47 74,59 61,60 59,73 47,68 40,78 33,68 21,73 19,60 6,59 10,47 0,40 10,33 6,21 19,20 21,7 33,12"/>
    </svg>
    <div class="abs b-upto center">UP TO</div>
    <div class="abs b-price center">$15</div>
    <div class="abs b-off center">OFF</div>
  </section>

</main>
</body>
</html>
```